Corvane Partners is a boutique consultancy focused on CXO-level advisory on strategy, operations, and organization in the Consumer Packaged Goods and Retail sector.

Our typical clients are senior level executives (Typically SVP level or higher), who hire us to help solve strategic business challenges. Our consultants are typically charged out at very high rates (Typically $2,000 - $3,000 per day), therefore, our business cards need to convey a high end, classy, yet professional image, consistent with high value strategic consulting.

We would like to see designs and colors that convey excellence, competence, and growth.

Our name 'Corvane' is derived from the Native American name of Mt. McKinley, the highest peak in North America. We would like to have a logo on our business card, that is simple yet conveys the aspirational nature of what we offer, i.e enabling the achievement of high performance.

Boutique

Corvane Partners, LLC
4417 Hollister Avenue Northwest, Suite 620
Washington, District of Columbia, 20016
United States
Mobile: +1 202 555 0148
ilsa.brenner@corvanepartnersllc.example

```html
<!DOCTYPE html>
<html lang="en">
<head>
<meta charset="utf-8">
<title>Corvane Partners LLC — Business Card</title>
<link href="https://fonts.googleapis.com/css2?family=Arimo:wght@400;700&display=swap" rel="stylesheet">
<style>
  :root {
    --backdrop: #ececec;
    --card: #ffffff;
    --ink: #1a1a1a;
    --accent: #d71920;
    --muted: #2b2b2b;
  }
  html, body {
    margin: 0;
    width: 1200px;
    height: 864px;
    overflow: hidden;
    background: var(--backdrop);
    font-family: "Arimo", Arial, sans-serif;
  }
  .business-card {
    position: absolute;
    left: 75px;
    top: 132px;
    width: 1050px;
    height: 600px;
    background: var(--card);
    box-shadow: 0 10px 30px rgba(0,0,0,0.12);
    color: var(--ink);
  }
  .brand-name {
    position: absolute;
    left: 90px;
    top: 170px;
    margin: 0;
    font-size: 56px;
    font-weight: 700;
    letter-spacing: 0.5px;
    color: var(--ink);
  }
  .holder {
    position: absolute;
    right: 60px;
    top: 250px;
    text-align: right;
  }
  .holder-name {
    margin: 0;
    font-size: 40px;
    font-weight: 400;
    color: var(--accent);
  }
  .holder-title {
    margin: 4px 0 0;
    font-size: 24px;
    color: var(--muted);
  }
  .address {
    position: absolute;
    right: 60px;
    top: 410px;
    margin: 0;
    text-align: right;
    font-style: normal;
    font-size: 24px;
    line-height: 1.3;
    color: var(--muted);
  }
  .contact {
    position: absolute;
    left: 90px;
    top: 495px;
    margin: 0;
    padding: 0;
    list-style: none;
    font-size: 24px;
    color: var(--muted);
  }
  .contact li {
    display: flex;
    align-items: center;
    gap: 16px;
    margin-bottom: 14px;
  }
  .contact svg { width: 22px; height: 22px; fill: var(--accent); flex: none; }
</style>
</head>
<body>
  <article class="business-card">
    <h1 class="brand-name">Corvane Partners LLC</h1>

    <div class="holder">
      <p class="holder-name">Ilsa Brenner</p>
      <p class="holder-title">Managing Partner</p>
    </div>

    <address class="address">
      4417 Hollister Avenue Northwest, Suite 620<br>
      Washington,District of Columbia 20016<br>
      United States
    </address>

    <ul class="contact">
      <li>
        <svg viewBox="0 0 24 24" aria-hidden="true"><circle cx="12" cy="7" r="5"/><path d="M2 23c0-6 4.5-9 10-9s10 3 10 9z"/></svg>
        <span>+1 202 555 0148</span>
      </li>
      <li>
        <svg viewBox="0 0 24 24" aria-hidden="true"><rect x="1" y="4" width="22" height="16"/><path d="M1 4l11 9 11-9" fill="none" stroke="#fff" stroke-width="2"/></svg>
        <span>ilsa.brenner@corvanepartnersllc.example</span>
      </li>
    </ul>
  </article>
</body>
</html>
```